Tamsel Naturopathics business card design

Using the tamsel logo designed, we would like that incorporated into a business card. A colour scheme which works with the logo and lists the following business details:

Lowen Tamsel - Naturopath
Level 1, 57 Orrick Street
Wollongong NSW
(02) 4813 7096
www.lowentamselnaturo.example

We would also like space on the back of the card for next appointment times.

Target Market(s)

Anyone looking to improve their health

Industry/Entity Type

Business

Requirements
Must have
• Tamsel Naturopathics logo, business details.
Nice to have
• Good colour schemes, attractive, eye-catching features that are easy to read.

```html
<!DOCTYPE html>
<html lang="en">
<head>
<meta charset="utf-8">
<title>Tamsel Naturopathics – Business Card</title>
<link rel="stylesheet" href="https://fonts.googleapis.com/css2?family=Questrial&family=Montserrat:wght@700&display=swap">
<style>
  :root {
    --bg: #e9e8ee;
    --paper: #ffffff;
    --ink: #4a4a4c;
    --ink-soft: #7a7a7e;
    --rule: #9a9aa0;
    --blue-deep: #1f5193;
    --blue-mid: #2a78bb;
    --blue-light: #3aa2da;
    --white: #ffffff;
    --white-soft: rgba(255,255,255,0.82);
  }
  * { box-sizing: border-box; margin: 0; padding: 0; }
  html, body {
    width: 1200px; height: 934px; overflow: hidden;
    background: var(--bg);
    font-family: "Questrial", "Century Gothic", sans-serif;
  }
  .sheet {
    width: 1200px; height: 934px;
    display: flex; align-items: center; justify-content: center; gap: 40px;
  }
  .card {
    width: 540px; height: 330px; position: relative;
    box-shadow: 0 6px 18px rgba(0,0,0,0.12);
    overflow: hidden;
  }

  /* Back: appointments */
  .card-back {
    background: var(--paper);
    display: grid; grid-template-columns: 220px 1fr;
    padding: 40px 26px 36px 30px; color: var(--ink);
  }
  .identity { display: flex; flex-direction: column; align-items: center; text-align: center; }
  .wordmark {
    margin-top: 44px;
    font-size: 26px; line-height: 1.15; letter-spacing: 2px;
    color: var(--ink); text-transform: uppercase;
  }
  .contact { margin-top: 34px; font-size: 12.5px; line-height: 1.35; color: var(--ink); }
  .contact .label { font-weight: 700; }

  .appointments { padding-left: 14px; }
  .appointments h2 {
    font-family: "Montserrat", sans-serif; font-weight: 700;
    font-size: 14px; color: var(--ink-soft); text-align: center; margin-bottom: 20px;
  }
  .slots { list-style: none; }
  .slot {
    display: flex; align-items: flex-end; gap: 5px;
    font-size: 11.5px; color: var(--ink-soft); margin-bottom: 19px;
  }
  .blank { display: inline-block; border-bottom: 1px solid var(--rule); height: 10px; }
  .blank.hour { width: 20px; }
  .blank.name { flex: 1; }
  .blank.d { width: 18px; }

  /* Front: name */
  .card-front {
    background: linear-gradient(160deg, var(--blue-light) 0%, var(--blue-mid) 40%, var(--blue-deep) 100%);
    color: var(--white);
    display: flex; flex-direction: column; align-items: center;
  }
  .card-front .wordmark {
    margin-top: 100px; color: var(--white); font-size: 30px;
  }
  .person { margin-top: 64px; text-align: center; }
  .person-name {
    font-family: "Montserrat", sans-serif; font-weight: 700;
    font-size: 15px; letter-spacing: 0.5px; text-transform: uppercase;
  }
  .person-role { font-size: 13px; color: var(--white-soft); margin-top: 2px; }
</style>
</head>
<body>
<main class="sheet">

  <section class="card card-back" aria-label="Card back with appointment times">
    <div class="identity">
      <p class="wordmark">Tamsel<br>Naturopathics</p>
      <address class="contact">
        www.lowentamselnaturo.example<br>
        Level 1, 57 Orrick Street<br>
        Wollongong NSW<br>
        <span class="label">T</span> (02) 4813 7096
      </address>
    </div>
    <div class="appointments">
      <h2>Your Appointments</h2>
      <ol class="slots">
        <li class="slot">1. <span class="blank hour"></span>am / pm <span class="blank name"></span><span class="blank d"></span>/<span class="blank d"></span>/<span class="blank d"></span></li>
        <li class="slot">2. <span class="blank hour"></span>am / pm <span class="blank name"></span><span class="blank d"></span>/<span class="blank d"></span>/<span class="blank d"></span></li>
        <li class="slot">3. <span class="blank hour"></span>am / pm <span class="blank name"></span><span class="blank d"></span>/<span class="blank d"></span>/<span class="blank d"></span></li>
        <li class="slot">4. <span class="blank hour"></span>am / pm <span class="blank name"></span><span class="blank d"></span>/<span class="blank d"></span>/<span class="blank d"></span></li>
        <li class="slot">5. <span class="blank hour"></span>am / pm <span class="blank name"></span><span class="blank d"></span>/<span class="blank d"></span>/<span class="blank d"></span></li>
      </ol>
    </div>
  </section>

  <section class="card card-front" aria-label="Card front">
    <p class="wordmark">Tamsel<br>Naturopathics</p>
    <div class="person">
      <p class="person-name">Lowen Tamsel</p>
      <p class="person-role">Naturopath</p>
    </div>
  </section>

</main>
</body>
</html>
```